Food item ad for Copper Comet Restaurant

We need visual appealing poster for our restaurant food items, for 6 categories.
1. kebabs
-tandoori chicken tikka
- tandoori 1/2 chicken
-chicken seekh
- Chaplee chicken
- Multani lamb
- lamb bouti
- lamb chops
2. Meat lover gravy dishes
- Kadai chicken masala
- butter chicken boneless
- butter chicken
- Multani kofta curry
- lamb curry
- afghani haryali lamb
3. Try this @ Copper comet
- lamb Palou
- keema mantu
- meat thali
- kebob wraps
- chicken rolls
- sweet rice
- keema lasagna
- Romani roti
4. For vegetarian lovers
- 8 or 9 items pick n choose thali
- vegitarian
- vegitarian mantu
- aloo tikki cholay
- aloo tikki burger
- vada pav
- pav bhaji
- mix veg pakoras
5. Snakers
- sweet BBQ corn on the cob
- cassava fried
- cassava baked
- bhel puri
- sev puri
- chaat papri
- pain puri
6. Hot n cold
- Kashmiri tea. Mango milk shake
- Indian masala tea. Lessi
- English tea. Fresh juices
- green tea Fresh lime soda
- Indian style coffee Mint lime soda
We need six poster 1 for each category
it can be simple and similar theme in all six posters
the idea is to introduce the menu from my 2 Feet x 4 feet poster hanging from the window
facing the street
you go to the website:
pls take out 8-9 items in vegetarian lovers and also the word vegetarian
Restaurant
Requirements
Must have
- Copper comet chef logo attached
Some food graphics
- kebabs
- rice
- Romani roti
-Naan
Kitchen equipment graphics
- tandoor ( Indian clay oven )
-Grill
Fire, charcoal, spice ,lime etc
Copper comet color theme ,,,,,see attachments
food item names to give customer info about the menu

```html
<!DOCTYPE html>
<html lang="en">
<head>
<meta charset="utf-8">
<title>Hot &amp; Cold – Copper Comet Restaurant</title>
<link href="https://fonts.googleapis.com/css2?family=Kavoon&family=Audiowide&family=Cormorant+Garamond:ital,wght@1,500&display=swap" rel="stylesheet">
<style>
  :root {
    --paper: #ffffff;
    --hot-orange: #f6a400;
    --amp-brown: #7a3410;
    --cold-teal: #14a0b4;
    --brand-gold: #e8c400;
    --brand-ink: #1a1a1a;
    --ember-red: #e8442a;
    --ember-glow: #f7a23c;
    --ash-grey: #9a9893;
    --clay: #d6cfc4;
    --menu-ink: #3b2414;
  }
  * { margin: 0; padding: 0; box-sizing: border-box; }
  html, body {
    width: 1200px;
    height: 2400px;
    overflow: hidden;
    background: var(--paper);
  }
  .poster {
    position: relative;
    width: 1200px;
    height: 2400px;
    background: var(--paper);
    overflow: hidden;
  }
  .headline {
    position: absolute;
    left: 0;
    width: 100%;
    text-align: center;
    line-height: 1;
    font-weight: 400;
  }
  .headline--hot {
    top: 100px;
    font-family: "Kavoon", cursive;
    font-size: 190px;
    color: var(--hot-orange);
    letter-spacing: 8px;
  }
  .headline--amp {
    top: 285px;
    font-family: "Cormorant Garamond", serif;
    font-style: italic;
    font-weight: 500;
    font-size: 150px;
    color: var(--amp-brown);
  }
  .headline--cold {
    top: 425px;
    font-family: "Audiowide", sans-serif;
    font-size: 150px;
    color: var(--cold-teal);
    letter-spacing: 6px;
  }
  .brand {
    position: absolute;
    top: 610px;
    left: 0;
    width: 100%;
    display: flex;
    flex-direction: column;
    align-items: center;
    gap: 50px;
  }
  .brand__mark {
    width: 300px;
    height: 300px;
    border-radius: 50%;
    background: var(--brand-ink);
  }
  .brand__name {
    font-family: "Audiowide", sans-serif;
    font-size: 58px;
    line-height: 1;
    color: var(--brand-gold);
    letter-spacing: 2px;
  }
  .tandoor-photo {
    position: absolute;
    left: 0;
    top: 1150px;
    width: 1200px;
    height: 1250px;
    background:
      radial-gradient(ellipse 46% 26% at 58% 34%, var(--ember-glow) 0%, var(--ember-red) 30%, #5a4a46 62%, transparent 80%),
      linear-gradient(180deg, rgba(255,255,255,1) 0%, rgba(200,195,188,0.6) 5%, var(--ash-grey) 12%, #6f6b66 34%, var(--clay) 60%, var(--clay) 100%);
  }
  .drinks {
    position: absolute;
    left: 100px;
    top: 1920px;
    width: 1000px;
    display: flex;
    justify-content: space-between;
  }
  .drinks__column { width: 470px; }
  .drinks__heading {
    font-family: "Audiowide", sans-serif;
    font-size: 52px;
    line-height: 1;
    margin-bottom: 26px;
    letter-spacing: 2px;
  }
  .drinks__heading--hot { color: #c97f00; }
  .drinks__heading--cold { color: var(--cold-teal); }
  .drinks__list { list-style: none; }
  .drinks__item {
    font-family: "Audiowide", sans-serif;
    font-size: 34px;
    line-height: 1.55;
    color: var(--menu-ink);
  }
</style>
</head>
<body>
  <main class="poster">
    <h1 class="headline headline--hot">HOT</h1>
    <div class="headline headline--amp">&amp;</div>
    <h2 class="headline headline--cold">COLD</h2>

    <div class="brand">
      <div class="brand__mark" aria-hidden="true"></div>
      <div class="brand__name">Copper Comet</div>
    </div>

    <div class="tandoor-photo" role="img" aria-label="Photograph of glowing charcoal embers inside a clay tandoor oven"></div>

    <section class="drinks" aria-label="Hot and cold drinks menu">
      <div class="drinks__column">
        <h3 class="drinks__heading drinks__heading--hot">Hot</h3>
        <ul class="drinks__list">
          <li class="drinks__item">Kashmiri Tea</li>
          <li class="drinks__item">Indian Masala Tea</li>
          <li class="drinks__item">English Tea</li>
          <li class="drinks__item">Green Tea</li>
          <li class="drinks__item">Indian Style Coffee</li>
        </ul>
      </div>
      <div class="drinks__column">
        <h3 class="drinks__heading drinks__heading--cold">Cold</h3>
        <ul class="drinks__list">
          <li class="drinks__item">Mango Milk Shake</li>
          <li class="drinks__item">Lassi</li>
          <li class="drinks__item">Fresh Juices</li>
          <li class="drinks__item">Fresh Lime Soda</li>
          <li class="drinks__item">Mint Lime Soda</li>
        </ul>
      </div>
    </section>
  </main>
</body>
</html>
```